HearthBay business card and stationary design

We are looking for a simple yet elegant design for our mortgage company business card and stationary.

The card should include:
Name (Doug Warley)
Title (CEO)
Phone Number (614-382-9047)
Address (48 Birchwood Terrace, Suite 315, Marlow, NJ 08214)
Email (email@hearthbay.example)
"NMLS" i.e. (NMLS 61947)
"Company NMLS" (Company NMLS 492716)

Contact Information for Business Card

See above

```html
<!DOCTYPE html>
<html lang="en">
<head>
<meta charset="utf-8">
<title>HearthBay Business Card</title>
<link rel="stylesheet" href="https://fonts.googleapis.com/css2?family=Roboto:wght@400;500;700&display=swap">
<style>
  :root {
    --bg: #ebe9e7;
    --navy: #101d2b;
    --blue: #239ad6;
    --ink: #2c2f33;
    --paper: #f6f6f6;
    --rule: #3a3f45;
  }
  * { box-sizing: border-box; margin: 0; padding: 0; }
  html, body {
    width: 1200px; height: 959px; overflow: hidden;
    background: var(--bg);
    font-family: "Roboto", Arial, sans-serif;
  }
  .canvas { position: relative; width: 1200px; height: 959px; }

  .card {
    position: absolute;
    width: 520px; height: 297px;
    border-radius: 2px;
    box-shadow: 0 10px 28px rgba(0,0,0,0.14), 0 2px 5px rgba(0,0,0,0.08);
    overflow: hidden;
  }

  /* Back face */
  .card--back {
    left: 110px; top: 90px;
    background: var(--navy);
    display: flex; align-items: center; justify-content: center;
  }
  .card--back .brand-name {
    font-size: 58px; font-weight: 500; color: #ffffff; letter-spacing: 0.5px;
  }

  /* Front face */
  .card--front {
    left: 570px; top: 520px;
    background: var(--paper);
  }
  .card--front .brand-name {
    position: absolute; left: 34px; top: 124px;
    font-size: 38px; font-weight: 500; color: var(--navy); letter-spacing: 0.3px;
  }
  .divider-short {
    position: absolute; left: 262px; top: 70px;
    width: 2px; height: 26px; background: var(--navy);
  }
  .divider-long {
    position: absolute; left: 276px; top: 104px;
    width: 1px; height: 130px; background: var(--rule);
  }
  .person {
    position: absolute; left: 276px; top: 62px;
  }
  .person-name {
    font-size: 17px; font-weight: 700; color: var(--navy); letter-spacing: 0.2px; line-height: 1;
  }
  .person-name .surname { color: var(--blue); }
  .person-title {
    margin-top: 3px; margin-left: 16px;
    font-size: 13px; font-weight: 700; color: var(--blue);
  }
  .contact {
    position: absolute; left: 290px; top: 104px;
    font-size: 12px; color: var(--ink); line-height: 1.35;
  }
  .contact .label { color: var(--blue); font-weight: 500; }
  .contact-list { list-style: none; margin-top: 4px; }
  .contact-list li { display: flex; align-items: center; gap: 7px; }
  .contact-list svg { width: 11px; height: 11px; fill: var(--blue); flex: none; }
  .band { position: absolute; left: 0; bottom: 0; width: 520px; height: 16px; }
</style>
</head>
<body>
<main class="canvas">

  <section class="card card--back" aria-label="Card back">
    <span class="brand-name">HearthBay</span>
  </section>

  <section class="card card--front" aria-label="Card front">
    <span class="brand-name">HearthBay</span>

    <span class="divider-short"></span>
    <span class="divider-long"></span>

    <div class="person">
      <p class="person-name">DOUG <span class="surname">WARLEY</span></p>
      <p class="person-title">CEO</p>
    </div>

    <div class="contact">
      <p><span class="label">NMLS</span> 61947</p>
      <p><span class="label">Company NMLS</span> 492716</p>
      <p>48 Birchwood Terrace,</p>
      <p>Suite 315, Marlow, NJ 08214</p>
      <ul class="contact-list">
        <li>
          <svg viewBox="0 0 24 24" aria-hidden="true"><path d="M6.6 10.8a15.1 15.1 0 0 0 6.6 6.6l2.2-2.2c.3-.3.7-.4 1-.2 1.1.4 2.3.6 3.6.6.6 0 1 .4 1 1V20c0 .6-.4 1-1 1A17 17 0 0 1 3 4c0-.6.4-1 1-1h3.5c.6 0 1 .4 1 1 0 1.3.2 2.5.6 3.6.1.3 0 .7-.2 1z"/></svg>
          614-382-9047
        </li>
        <li>
          <svg viewBox="0 0 24 24" aria-hidden="true"><path d="M2 5h20v14H2z M2 5l10 8 10-8" fill="none" stroke="#239ad6" stroke-width="2.4"/></svg>
          email@hearthbay.example
        </li>
        <li>
          <svg viewBox="0 0 24 24" aria-hidden="true"><circle cx="12" cy="12" r="9.5" fill="none" stroke="#239ad6" stroke-width="2"/><path d="M2.5 12h19M12 2.5c3 3 3 16 0 19M12 2.5c-3 3-3 16 0 19" fill="none" stroke="#239ad6" stroke-width="1.6"/></svg>
          www.hearthbay.example
        </li>
      </ul>
    </div>

    <svg class="band" viewBox="0 0 520 16" preserveAspectRatio="none" aria-hidden="true">
      <polygon points="0,16 0,13 342,0 336,16" fill="var(--navy)"/>
      <polygon points="350,16 356,0 520,0 520,16" fill="var(--blue)"/>
    </svg>
  </section>

</main>
</body>
</html>
```